Upscale business cards needed for family office

We would like professional business cards created for employees of our family office. Relatively simple and straightforward, but also with a unique element to set them apart. Probably stick with neutral and simple colors that mesh well with the colors in the logo. We need space for the traditional elements, including name, title, address, email/phone number.

Industry/Entity Type

Business

Contact Information for Business Card

Space for name, title, phone number, email, address

```html
<!DOCTYPE html>
<html lang="en">
<head>
<meta charset="utf-8">
<title>Harlow &amp; Lane — Business Card</title>
<link rel="stylesheet" href="https://fonts.googleapis.com/css2?family=Open+Sans:wght@400;600&display=swap">
<style>
  :root {
    --stage: #000000;
    --card: #2f3034;
    --card-edge: #34353a;
    --divider: #3d3e43;
    --accent: #2a8fd6;
    --text: #e4e5e7;
    --mark-grey: #9a9ca0;
    --mark-square: #2a8fd6;
  }
  html, body {
    margin: 0;
    padding: 0;
    width: 1200px;
    height: 900px;
    overflow: hidden;
    background: var(--stage);
    font-family: "Open Sans", Arial, sans-serif;
  }
  .stage {
    position: relative;
    width: 1200px;
    height: 900px;
  }
  .card {
    position: absolute;
    top: 271px;
    width: 457px;
    height: 281px;
    border-radius: 14px;
    background: linear-gradient(180deg, var(--card-edge), var(--card));
  }
  .card--front { left: 137px; }
  .card--back  { left: 626px; }

  .brand {
    position: absolute;
    width: 112px;
    height: 124px;
    display: flex;
    flex-direction: column;
    align-items: center;
    justify-content: center;
    gap: 10px;
  }
  .card--front .brand { left: 75px; top: 67px; }
  .card--back .brand  { left: 169px; top: 75px; width: 120px; height: 131px; }
  .brand__square {
    width: 14px;
    height: 14px;
    background: var(--mark-square);
  }
  .brand__name {
    margin: 0;
    color: var(--mark-grey);
    font-size: 21px;
    font-weight: 600;
    line-height: 1.15;
    text-align: center;
  }

  .divider {
    position: absolute;
    left: 226px;
    top: 67px;
    width: 1px;
    height: 124px;
    background: var(--divider);
  }

  .details {
    position: absolute;
    left: 249px;
    top: 63px;
    color: var(--text);
    white-space: nowrap;
  }
  .details__name {
    margin: 0;
    color: var(--accent);
    font-size: 18px;
    font-weight: 600;
    line-height: 22px;
  }
  .details__title {
    margin: 0 0 11px;
    font-size: 12px;
    line-height: 16px;
  }
  .details__address {
    margin: 0 0 11px;
    font-size: 12px;
    line-height: 16px;
    font-style: normal;
  }
  .contact {
    list-style: none;
    margin: 0;
    padding: 0;
    font-size: 12px;
    line-height: 16.5px;
  }
  .contact__item {
    display: flex;
    align-items: center;
    gap: 7px;
  }
  .contact__icon {
    width: 10px;
    height: 10px;
    flex: none;
    fill: var(--accent);
    stroke: var(--accent);
  }
</style>
</head>
<body>
<main class="stage">
  <section class="card card--front">
    <div class="brand">
      <span class="brand__square"></span>
      <p class="brand__name">Harlow<br>&amp; Lane</p>
    </div>
    <span class="divider"></span>
    <div class="details">
      <h1 class="details__name">Daniel Whitford</h1>
      <p class="details__title">Managing Director</p>
      <address class="details__address">48 Harbour Row, Suite 200<br>Lakeport, Westland 20415.</address>
      <ul class="contact">
        <li class="contact__item">
          <svg class="contact__icon" viewBox="0 0 10 10"><path stroke="none" d="M2 0.5l1.6 2-1 1a5.5 5.5 0 0 0 3.9 3.9l1-1 2 1.6-1 1.5C4.5 9.5 0.5 5.5 0.5 1.5z"/></svg>
          <span>044-555 018 274</span>
        </li>
        <li class="contact__item">
          <svg class="contact__icon" viewBox="0 0 10 10"><path stroke="none" d="M0.5 2h9v6.5h-9z"/><path fill="none" stroke="#2f3034" stroke-width="0.9" d="M0.8 2.4L5 5.6l4.2-3.2"/></svg>
          <span>daniel@harlowlane.com</span>
        </li>
        <li class="contact__item">
          <svg class="contact__icon" viewBox="0 0 10 10"><path fill="none" stroke-width="1.2" d="M4.3 5.7l1.4-1.4M4 3.6l1.3-1.3a1.6 1.6 0 0 1 2.4 2.4L6.4 6M6 6.4L4.7 7.7a1.6 1.6 0 0 1-2.4-2.4L3.6 4"/></svg>
          <span>www.harlowlane.com</span>
        </li>
      </ul>
    </div>
  </section>

  <section class="card card--back">
    <div class="brand">
      <span class="brand__square"></span>
      <p class="brand__name">Harlow<br>&amp; Lane</p>
    </div>
  </section>
</main>
</body>
</html>
```